Plastic Business Card for Bookkeeper

We are looking for a simple professional business card design to use for printing on thin frosted plastic (see-through) card stock. Logo and brand guideline documents are attached as well as a photo of our old business card, and another business card example that we like.

Target Market(s)

Small Business

Industry/Entity Type

Bookkeeper

Contact Information for Business Card

Harriet Valdez CPA
Chief Executive Bookkeeper
T. 03 5926 4187
M. 0432 861 507
E. harriet@quillpathledger.com
W. www.quillpathledger.com

Font styles to use
Sans Serif

Colors
6b449b
00a990

Requirements
Must have
• Stick with logo colors. Writing should be clear and easy to read and not too cramped together.
Nice to have
• Tag line for back of the card - 'Not your ordinary Bookkeeper'

```html
<!DOCTYPE html>
<html lang="en">
<head>
<meta charset="utf-8">
<title>Harriet Valdez CPA – Business Card</title>
<link rel="stylesheet" href="https://fonts.googleapis.com/css2?family=Khand:wght@600&family=Roboto:wght@400&family=Montserrat:wght@600&display=swap">
<style>
  :root {
    --page-bg: #e6e4e1;
    --frost: #eef0f1;
    --frost-edge: #dfe2e4;
    --teal: #00a990;
    --teal-deep: #0f8f8f;
    --blue: #3a5fb4;
    --purple: #6b449b;
    --violet: #5a3fb0;
    --ink-light: #ffffff;
    --ink-soft: #f3e4ea;
  }
  * { margin: 0; padding: 0; box-sizing: border-box; }
  html, body {
    width: 1200px;
    height: 1054px;
    overflow: hidden;
    background: var(--page-bg);
  }
  .card {
    position: absolute;
    left: 100px;
    top: 225px;
    width: 1000px;
    height: 604px;
    background: linear-gradient(135deg, var(--frost) 0%, #f6f7f8 45%, var(--frost-edge) 100%);
    box-shadow: 0 10px 40px rgba(0,0,0,0.12);
    overflow: hidden;
  }
  .card__art {
    position: absolute;
    inset: 0;
    width: 1000px;
    height: 604px;
  }
  .identity {
    position: absolute;
    left: 37px;
    top: 58px;
    color: var(--ink-light);
  }
  .identity__name {
    font-family: "Khand", sans-serif;
    font-weight: 600;
    font-size: 40px;
    line-height: 1;
    letter-spacing: 0.3px;
  }
  .identity__title {
    font-family: "Roboto", sans-serif;
    font-size: 24px;
    margin-top: 10px;
    color: #eef0fb;
  }
  .contacts {
    position: absolute;
    left: 37px;
    top: 404px;
    list-style: none;
  }
  .contacts__item {
    display: flex;
    align-items: center;
    height: 38px;
    font-family: "Roboto", sans-serif;
    font-size: 25px;
    color: var(--ink-soft);
  }
  .contacts__icon {
    width: 22px;
    height: 22px;
    margin-right: 28px;
    flex: none;
  }
  .brand {
    position: absolute;
    left: 620px;
    top: 150px;
    width: 330px;
    text-align: center;
  }
  .brand__dot {
    width: 96px;
    height: 96px;
    border-radius: 50%;
    background: var(--teal-deep);
    margin: 0 auto 40px;
  }
  .brand__name {
    font-family: "Montserrat", sans-serif;
    font-weight: 600;
    font-size: 38px;
    line-height: 1.1;
    letter-spacing: 1px;
    color: var(--purple);
  }
</style>
</head>
<body>
  <div class="card">
    <svg class="card__art" viewBox="0 0 1000 604" aria-hidden="true">
      <defs>
        <linearGradient id="panelGradient" x1="0" y1="1" x2="0.9" y2="0">
          <stop offset="0" stop-color="#0e9a9a"/>
          <stop offset="0.45" stop-color="#3a64b8"/>
          <stop offset="1" stop-color="#5a3fb0"/>
        </linearGradient>
      </defs>
      <path d="M0 0 H588 C 495 150, 468 420, 588 604 H0 Z" fill="var(--purple)"/>
      <path d="M0 0 H572 C 478 150, 452 420, 566 604 H0 Z" fill="url(#panelGradient)"/>
      <path d="M552 72 C 505 190, 485 330, 508 470" fill="none" stroke="var(--teal-deep)" stroke-width="7" stroke-linecap="round"/>
      <path d="M554 50 L 536 84 L 568 80 Z" fill="var(--teal-deep)"/>
    </svg>

    <div class="identity">
      <div class="identity__name">Harriet Valdez CPA</div>
      <div class="identity__title">Chief Executive Bookkeeper</div>
    </div>

    <ul class="contacts">
      <li class="contacts__item">
        <svg class="contacts__icon" viewBox="0 0 24 24" fill="#f3e4ea"><path d="M3 9c0-3 4-5 9-5s9 2 9 5v2h-5V9H8v2H3z"/><rect x="5" y="12" width="14" height="9" rx="2"/></svg>
        03 5926 4187
      </li>
      <li class="contacts__item">
        <svg class="contacts__icon" viewBox="0 0 24 24" fill="none" stroke="#f3e4ea" stroke-width="2"><rect x="6" y="2" width="12" height="20" rx="2"/><line x1="10" y1="18" x2="14" y2="18"/></svg>
        0432 861 507
      </li>
      <li class="contacts__item">
        <svg class="contacts__icon" viewBox="0 0 24 24" fill="none" stroke="#f3e4ea" stroke-width="2"><rect x="2" y="5" width="20" height="14"/><path d="M2 5 L12 13 L22 5"/></svg>
        harriet@quillpathledger.com
      </li>
      <li class="contacts__item">
        <svg class="contacts__icon" viewBox="0 0 24 24" fill="none" stroke="#f3e4ea" stroke-width="1.8"><circle cx="12" cy="12" r="9"/><ellipse cx="12" cy="12" rx="4" ry="9"/><line x1="3" y1="12" x2="21" y2="12"/></svg>
        www.quillpathledger.com
      </li>
    </ul>

    <div class="brand">
      <div class="brand__dot"></div>
      <div class="brand__name">QUILLPATH<br>LEDGER</div>
    </div>
  </div>
</body>
</html>
```